online jewellery store business card

all black business card, glossy, with gold writing, gold logo and name (provided). simple design.

Target Market(s)

This business card is to put with purchases, so it just needs the logo and name Velmora Jewellery which I have uploaded pictures for you to use. Then it needs the web address, bidlorn address, email address and then the like us on KL for 10% off. All words to be used have been provided. Thanks

Industry/Entity Type

Store

Contact Information for Business Card

www.velmorajewellery.com
stores.bidlorn.com.au/Velmora-Jewellery
info@velmorajewellery.com

Like us on kinloop for 10% off your next purchase!

Requirements
Must have
• black background
gold writing
glossy look
Should not have
• yellow writing

```html
<!DOCTYPE html>
<html lang="en">
<head>
<meta charset="utf-8">
<title>Velmora Jewellery – Business Card</title>
<link rel="stylesheet" href="https://fonts.googleapis.com/css2?family=Josefin+Sans:wght@300&family=Open+Sans:wght@400;600;700&display=swap">
<style>
  :root {
    --page-bg: #ececec;
    --card-black: #050505;
    --logo-panel: #0b0b0b;
    --gold: #c9a55a;
    --gold-light: #f0d593;
    --gold-dark: #8a6a2c;
    --text-light: #d8d8d8;
    --text-white: #ffffff;
  }
  * { box-sizing: border-box; margin: 0; padding: 0; }
  html, body {
    width: 1200px; height: 709px; overflow: hidden;
    background: var(--page-bg);
  }
  .business-card {
    position: absolute; left: 100px; top: 55px;
    width: 1000px; height: 600px;
    background: var(--card-black);
    font-family: "Open Sans", sans-serif;
    overflow: hidden;
  }
  .gold-band {
    position: absolute; left: 0; width: 100%; height: 14px;
    background: linear-gradient(90deg, var(--gold-dark), var(--gold-light) 30%, var(--gold) 55%, var(--gold-light) 80%, var(--gold-dark));
  }
  .gold-band.top { top: 0; }
  .gold-band.bottom { bottom: 0; }
  .brand-panel {
    position: absolute; left: 60px; top: 78px;
    width: 316px; height: 290px;
    background: var(--logo-panel);
    text-align: center;
  }
  .brand-mark {
    display: block; margin: 24px auto 0;
  }
  .brand-name {
    font-family: "Josefin Sans", sans-serif;
    font-weight: 300;
    color: var(--gold);
    font-size: 40px;
    letter-spacing: 6px;
    line-height: 66px;
    margin-top: 8px;
  }
  .contact-list {
    position: absolute; left: 470px; top: 128px;
    list-style: none;
  }
  .contact-item {
    display: flex; align-items: flex-start;
    color: var(--gold);
    font-size: 25px; line-height: 40px;
  }
  .contact-item + .contact-item { margin-top: 66px; }
  .contact-icon {
    flex: none; width: 26px; height: 26px; border-radius: 50%;
    background: var(--gold);
    color: var(--card-black);
    font-size: 15px; font-weight: 700; line-height: 25px; text-align: center;
    margin: 7px 22px 0 0;
  }
  .thank-you {
    position: absolute; left: 0; top: 446px; width: 100%;
    text-align: center; font-size: 25px; font-weight: 600;
    color: var(--text-light);
  }
  .thank-you strong { color: var(--text-white); font-weight: 600; }
  .divider {
    position: absolute; left: 87px; top: 494px;
    width: 830px; height: 3px;
    background: linear-gradient(90deg, var(--gold-dark), var(--gold-light), var(--gold-dark));
  }
  .offer {
    position: absolute; left: 0; top: 508px; width: 100%;
    text-align: center; font-size: 25px; font-weight: 700;
    color: var(--text-light);
  }
  .offer strong { color: var(--text-white); font-weight: 700; }
</style>
</head>
<body>
  <article class="business-card">
    <div class="gold-band top"></div>

    <div class="brand-panel">
      <svg class="brand-mark" width="112" height="112" viewBox="0 0 112 112" aria-hidden="true">
        <circle cx="56" cy="56" r="52" fill="none" stroke="#c9a55a" stroke-width="2"/>
      </svg>
      <h1 class="brand-name">VELMORA<br>JEWELLERY</h1>
    </div>

    <ul class="contact-list">
      <li class="contact-item">
        <span class="contact-icon">w</span>
        <span>www.velmorajewellery.com<br>stores.bidlorn.com.au/Velmora-Jewellery</span>
      </li>
      <li class="contact-item">
        <span class="contact-icon">e</span>
        <span>info@velmorajewellery.com</span>
      </li>
    </ul>

    <p class="thank-you"><strong>THANK YOU</strong> FOR YOUR PURCHASE</p>
    <div class="divider"></div>
    <p class="offer">LIKE US ON KINLOOP FOR <strong>10% OFF</strong> YOUR NEXT PURCHASE!</p>

    <div class="gold-band bottom"></div>
  </article>
</body>
</html>
```